Business Card Design Project

I need a business card designed from scratch. I have an existing logo that I can upload in Illustrator for modification or redesign.

The Company is called Rank Harbor http://rankharbor.com.au and we provide Search Engine Optimization services to Australian businesses. The current logo signifies an increase in visitors, profits etc...

There are no restrictions as to the redesign - colours, style etc are all open to change.

Cards will be full colour and one sided printed at http://www.printlorvex.com.au so check their requirements for file format and sizes etc.

I will expect all original files upon completion of project.

Target Market(s)

Any business with a web site looking to improve their search engine rankings

Industry/Entity Type

Business

Requirements
Must have
• I like modern, sleek designs. Clean, not fussy, uncluttered.

```html
<!DOCTYPE html>
<html lang="en">
<head>
<meta charset="utf-8">
<title>Rank Harbor – Business Card</title>
<link rel="stylesheet" href="https://fonts.googleapis.com/css2?family=Open+Sans:wght@400;700&display=swap">
<style>
  :root {
    --backdrop: #3a3532;
    --card: #ffffff;
    --brand-blue: #1a73b8;
    --accent-yellow: #f2c81c;
    --text-grey: #7a7a7a;
    --rule-grey: #c9c9c9;
  }
  * { margin: 0; padding: 0; box-sizing: border-box; }
  html, body {
    width: 1200px;
    height: 900px;
    overflow: hidden;
    background: var(--backdrop);
    font-family: "Open Sans", Arial, sans-serif;
  }
  .business-card {
    position: absolute;
    left: 100px;
    top: 145px;
    width: 1000px;
    height: 610px;
    background: var(--card);
    box-shadow: 0 12px 30px rgba(0,0,0,0.35);
  }
  .brand {
    position: absolute;
    left: 60px;
    top: 92px;
    display: flex;
    align-items: center;
    gap: 18px;
  }
  .brand-dot {
    width: 46px;
    height: 46px;
    border-radius: 50%;
    background: var(--accent-yellow);
  }
  .brand-name {
    font-size: 54px;
    font-weight: 700;
    color: var(--brand-blue);
    line-height: 1;
    letter-spacing: -0.5px;
  }
  .holder-name {
    position: absolute;
    right: 60px;
    top: 238px;
    font-size: 30px;
    font-weight: 700;
    color: var(--brand-blue);
  }
  .divider-rule {
    position: absolute;
    left: 55px;
    right: 60px;
    top: 288px;
    height: 2px;
    background: var(--accent-yellow);
  }
  .holder-title {
    position: absolute;
    right: 60px;
    top: 296px;
    font-size: 22px;
    font-weight: 400;
    color: var(--text-grey);
  }
  .contact-list {
    position: absolute;
    left: 55px;
    bottom: 52px;
    display: flex;
  }
  .contact-icons {
    display: flex;
    flex-direction: column;
    width: 30px;
    padding-right: 12px;
    border-right: 2px solid var(--rule-grey);
  }
  .contact-icons svg {
    width: 20px;
    height: 20px;
    margin: 8px 0;
    fill: none;
    stroke: var(--brand-blue);
    stroke-width: 1.8;
  }
  .contact-lines {
    list-style: none;
    padding-left: 12px;
    font-size: 24px;
    line-height: 36px;
    color: var(--text-grey);
  }
</style>
</head>
<body>
  <div class="business-card">
    <div class="brand">
      <div class="brand-dot"></div>
      <div class="brand-name">Rank Harbor</div>
    </div>

    <div class="holder-name">Mark Ellison</div>
    <div class="divider-rule"></div>
    <div class="holder-title">Internet Marketing Consultant</div>

    <div class="contact-list">
      <div class="contact-icons">
        <svg viewBox="0 0 24 24" aria-label="Phone"><path d="M3 9c0-3 4-5 9-5s9 2 9 5l-4 1-1-3H8L7 10 3 9z" fill="var(--brand-blue)"/><rect x="6" y="12" width="12" height="7" rx="1.5" fill="var(--brand-blue)"/></svg>
        <svg viewBox="0 0 24 24" aria-label="Email"><rect x="3" y="6" width="18" height="12"/><path d="M3 6l9 7 9-7"/></svg>
        <svg viewBox="0 0 24 24" aria-label="Website"><circle cx="12" cy="12" r="9"/><ellipse cx="12" cy="12" rx="4" ry="9"/><path d="M3 12h18M5 7h14M5 17h14"/></svg>
      </div>
      <ul class="contact-lines">
        <li>1300 482915</li>
        <li>mark@rankharbor.com.au</li>
        <li>www.rankharbor.com.au</li>
      </ul>
    </div>
  </div>
</body>
</html>
```